Lena Corvell Business Card

I need a business card that reflects my current website: itslenacorvell.example and screenshot attached. If we keep the color scheme of the site and sample card below that would be ideal. The business card should include the information on the attached sample cards.

Industry/Entity Type

Business

```html
<!DOCTYPE html>
<html lang="en">
<head>
<meta charset="utf-8">
<title>Lena Corvell Business Card</title>
<link href="https://fonts.googleapis.com/css2?family=Lato:wght@400;700&display=swap" rel="stylesheet">
<style>
  :root {
    --backdrop: #2b2b2b;
    --card: #151515;
    --teal: #5fc2b0;
    --ink: #f2f2f2;
  }
  * { margin: 0; padding: 0; box-sizing: border-box; }
  html, body { width: 1200px; height: 1000px; overflow: hidden; }
  body {
    background: var(--backdrop);
    font-family: "Lato", sans-serif;
    position: relative;
  }
  .business-card {
    position: absolute;
    left: 150px; top: 240px;
    width: 900px; height: 520px;
    background: var(--card);
    border-radius: 22px;
    box-shadow: 0 20px 50px rgba(0,0,0,.5);
    color: var(--ink);
    text-align: center;
  }
  .brand-mark {
    position: absolute;
    top: 110px; left: 0; right: 0;
    font-size: 76px;
    font-weight: 400;
    color: var(--teal);
    letter-spacing: 1px;
  }
  .holder-name {
    position: absolute;
    top: 262px; left: 0; right: 0;
    font-size: 28px;
    font-weight: 700;
    color: var(--teal);
    letter-spacing: 1px;
  }
  .detail-row {
    position: absolute;
    left: 0; right: 0;
    display: flex;
    justify-content: center;
    align-items: center;
    gap: 28px;
    font-size: 21px;
  }
  .detail-row.roles { top: 314px; }
  .detail-row.contacts { top: 360px; }
  .detail-row.socials { top: 408px; gap: 16px; }
  .detail { display: inline-flex; align-items: center; gap: 8px; }
  .icon { width: 22px; height: 22px; flex: none; }
  .social-dot { width: 22px; height: 22px; border-radius: 50%; background: var(--teal); }
</style>
</head>
<body>
  <section class="business-card">
    <div class="brand-mark">its Lena Corvell</div>
    <h1 class="holder-name">LENA CORVELL</h1>

    <div class="detail-row roles">
      <span class="detail">Brand Curator, Digital Storyteller, Social Entreprenuer</span>
      <span class="detail">
        <svg class="icon" viewBox="0 0 24 24" fill="none" stroke="#5fc2b0" stroke-width="2">
          <circle cx="12" cy="12" r="10"/><ellipse cx="12" cy="12" rx="4" ry="10"/><line x1="2" y1="12" x2="22" y2="12"/>
        </svg>
        www.itslenacorvell.example
      </span>
    </div>

    <div class="detail-row contacts">
      <span class="detail">
        <svg class="icon" viewBox="0 0 24 24" fill="#5fc2b0">
          <path d="M6.6 10.8a15 15 0 0 0 6.6 6.6l2.2-2.2a1 1 0 0 1 1-.25 11.4 11.4 0 0 0 3.6.57 1 1 0 0 1 1 1V20a1 1 0 0 1-1 1A17 17 0 0 1 3 4a1 1 0 0 1 1-1h3.5a1 1 0 0 1 1 1c0 1.25.2 2.45.57 3.57a1 1 0 0 1-.25 1z"/>
        </svg>
        555.014.2290
      </span>
      <span class="detail">
        <svg class="icon" viewBox="0 0 24 24" fill="none" stroke="#5fc2b0" stroke-width="2">
          <rect x="2" y="5" width="20" height="14" rx="1"/><polyline points="2,5 12,13 22,5"/>
        </svg>
        me@lenacorvell.example
      </span>
      <span class="detail">
        <span class="social-dot"></span>
        @itslenacorvell.example
      </span>
    </div>

    <div class="detail-row socials">
      <span class="social-dot"></span>
      <span class="social-dot"></span>
    </div>
  </section>
</body>
</html>
```